Modern Website Template

We need a set of modern website templates and would like to see what you can come up with.

The template should be easily customizable by an end user so they can easily swap out generic images with their own image if needed.

Some examples of templates you can create would be;
Small Business
Lawyer
Teacher
Birthday Party
Real Estate Agent
Doctor
Travel
Sports
Wedding
Religious

If we like your work we will be looking for more templates to be created.

**TEMPLATE MUST BE ORIGINAL AND NOT RESOLD**

Industry/Entity Type

Business

```html
<!DOCTYPE html>
<html lang="en">
<head>
<meta charset="utf-8">
<title>Northlane – Business Template</title>
<link href="https://fonts.googleapis.com/css2?family=Raleway:wght@400;500;600&display=swap" rel="stylesheet">
<style>
  :root {
    --blue: #3d93dc;
    --blue-soft: #6eabe2;
    --green-top: #b0d043;
    --green-bottom: #8cb627;
    --ink: #1c1c1c;
    --muted: #777;
    --rule: #dedede;
    --hero-bg: #ececec;
    --lower-bg: #f6f7f9;
    --orange: #f0622a;
    --lime: #a5c63b;
  }
  * { box-sizing: border-box; margin: 0; padding: 0; }
  html, body { width: 1200px; height: 1000px; overflow: hidden; }
  body { font-family: "Raleway", sans-serif; background: #fff; color: var(--ink); position: relative; }

  .site-header { position: absolute; top: 0; left: 0; width: 1200px; height: 97px; background: #fff; border-bottom: 1px solid var(--rule); }
  .brand { position: absolute; left: 110px; top: 36px; display: flex; align-items: center; gap: 10px; color: var(--blue); font-size: 21px; font-weight: 500; line-height: 26px; }
  .brand-dot { width: 18px; height: 18px; background: #8ec0ea; border-radius: 50%; }
  .btn-login { position: absolute; left: 850px; top: 28px; width: 239px; height: 39px; border-radius: 4px; background: linear-gradient(var(--green-top), var(--green-bottom)); border: 1px solid #86ad25; color: #fff; font-size: 15px; display: flex; align-items: center; justify-content: center; }

  .hero { position: absolute; top: 97px; left: 0; width: 1200px; height: 367px; background: var(--hero-bg); border-bottom: 1px solid #d6d6d6; overflow: hidden; }
  .hero-title { position: absolute; top: 24px; width: 100%; text-align: center; font-size: 46px; font-weight: 600; line-height: 56px; color: var(--ink); }
  .hero-sub { position: absolute; top: 81px; width: 100%; text-align: center; font-size: 16px; line-height: 20px; color: var(--blue-soft); }
  .hero-showcase { position: absolute; left: 225px; top: 134px; width: 760px; height: 233px; border-radius: 10px 10px 0 0;
    background: linear-gradient(90deg, #f4f4f4 0%, #eaeaea 17%, #2b2b2b 18%, #1f1f1f 50%, #2b2b2b 81%, #eaeaea 82%, #f4f4f4 100%); }

  .cta-group { position: absolute; left: 395px; top: 494px; display: flex; height: 42px; }
  .btn-buy { width: 210px; background: linear-gradient(var(--green-top), var(--green-bottom)); border: 1px solid #86ad25; border-radius: 4px 0 0 4px; color: #fff; font-size: 18.5px; display: flex; align-items: center; justify-content: center; }
  .btn-trial { width: 191px; background: linear-gradient(#fff, #f2f2f2); border: 1px solid #cfcfcf; border-left: none; border-radius: 0 4px 4px 0; color: var(--ink); font-size: 18.5px; display: flex; align-items: center; justify-content: center; }

  .service { position: absolute; top: 586px; width: 315px; }
  .service-head { display: flex; align-items: center; gap: 10px; height: 26px; }
  .service-title { font-size: 18.5px; font-weight: 500; }
  .service-text { margin-top: 10px; font-size: 11.5px; line-height: 20px; color: var(--muted); }
  .read-more { font-size: 11.5px; line-height: 20px; color: #333; }
  .read-more a { color: var(--blue); text-decoration: underline; }

  .features { position: absolute; top: 758px; left: 0; width: 1200px; height: 242px; background: var(--lower-bg); border-top: 1px solid var(--rule); }
  .features-title { position: absolute; left: 110px; top: 42px; font-size: 22px; font-weight: 500; line-height: 28px; }
  .feature-list { list-style: none; position: absolute; left: 110px; top: 105px; }
  .feature-list li { display: flex; align-items: center; gap: 15px; height: 20px; margin-bottom: 25px; font-size: 12px; color: #111; }
  .tick { width: 20px; height: 20px; flex: none; }
</style>
</head>
<body>
  <header class="site-header">
    <div class="brand"><span class="brand-dot"></span>Northlane</div>
    <div class="btn-login">Login to Customer Area</div>
  </header>

  <section class="hero">
    <h1 class="hero-title">Some Catchy Text Goes Here</h1>
    <p class="hero-sub">Lorem ipsum dolor sit amet, consectetur adipiscing elit</p>
    <div class="hero-showcase" role="img" aria-label="Product showcase: laptop and tablets displaying dashboard charts"></div>
  </section>

  <div class="cta-group">
    <div class="btn-buy">Buy Now for $20</div>
    <div class="btn-trial">Sign up for Trial</div>
  </div>

  <article class="service" style="left:107px">
    <div class="service-head">
      <svg width="26" height="26" viewBox="0 0 26 26"><path d="M2 14 C5 -2 9 -2 12 13 C15 28 20 28 24 10" fill="none" stroke="var(--blue)" stroke-width="2"/></svg>
      <span class="service-title">Service 1</span>
    </div>
    <p class="service-text">Aipit molestie diam ut lacinia. Lorem ipsum dolor sit amet, consectetur adipiscing elit. Etiam at euismod dui. Curabitur sit amet accumsan metus. Aenean interdum pellentesque tristique.</p>
    <p class="read-more">• <a>Read More</a></p>
  </article>

  <article class="service" style="left:446px">
    <div class="service-head">
      <svg width="18" height="20" viewBox="0 0 18 20"><rect x="0" y="8" width="4" height="11" fill="var(--orange)"/><path d="M5 8 L9 1 Q11 0 11 3 L10 7 L16 7 Q18 8 17 10 L15 18 Q14 19 12 19 L5 19 Z" fill="var(--orange)"/></svg>
      <span class="service-title">Service 2</span>
    </div>
    <p class="service-text">Aipit molestie diam ut lacinia. Lorem ipsum dolor sit amet, consectetur adipiscing elit. Etiam at euismod dui. Curabitur sit amet accumsan metus. Aenean interdum pellentesque tristique.</p>
    <p class="read-more">• <a>Read More</a></p>
  </article>

  <article class="service" style="left:778px">
    <div class="service-head">
      <svg width="22" height="20" viewBox="0 0 22 20"><rect x="1" y="2" width="5" height="17" fill="var(--lime)"/><rect x="8" y="6" width="5" height="13" fill="var(--lime)"/><rect x="15" y="10" width="5" height="9" fill="var(--lime)"/></svg>
      <span class="service-title">Service 3</span>
    </div>
    <p class="service-text">Aipit molestie diam ut lacinia. Lorem ipsum dolor sit amet, consectetur adipiscing elit. Etiam at euismod dui. Curabitur sit amet accumsan metus. Aenean interdum pellentesque tristique.</p>
    <p class="read-more">• <a>Read More</a></p>
  </article>

  <section class="features">
    <h2 class="features-title">We are an award-winning company that fouses on:</h2>
    <ul class="feature-list">
      <li><svg class="tick" viewBox="0 0 20 20"><circle cx="10" cy="10" r="10" fill="var(--green-bottom)"/><path d="M6 10 L9 13 L14 7" fill="none" stroke="#fff" stroke-width="2"/></svg>&nbsp;Pellentesque sit amet enim risus, non iaculis metus.</li>
      <li><svg class="tick" viewBox="0 0 20 20"><circle cx="10" cy="10" r="10" fill="var(--green-bottom)"/><path d="M6 10 L9 13 L14 7" fill="none" stroke="#fff" stroke-width="2"/></svg>Pellentesque id sem in nulla ultricies porttitor.</li>
      <li><svg class="tick" viewBox="0 0 20 20"><circle cx="10" cy="10" r="10" fill="var(--green-bottom)"/><path d="M6 10 L9 13 L14 7" fill="none" stroke="#fff" stroke-width="2"/></svg>Nulla ullamcorper quam neque, sed ornare tellus.</li>
      <li><svg class="tick" viewBox="0 0 20 20"><circle cx="10" cy="10" r="10" fill="var(--green-bottom)"/><path d="M6 10 L9 13 L14 7" fill="none" stroke="#fff" stroke-width="2"/></svg>Curabitur vitae lectus eu arcu tempor dictum.</li>
    </ul>
  </section>
</body>
</html>
```